KinLetter Consumer (B2C) Website for Ethical Wills

Meet the “Parrow” family. A few weeks before Thanksgiving, the 40-year-old, healthy father and husband decided to take a nap after church. Hours later, the mom ‘nudged’ her husband to wake him, however, she was unable to do so. Unfortunately, he unexpectedly passed away during his nap. His four children (ages 16, 14, 12 & 10) and wife were left to navigate their lives without the wisdom and guidance of a loving dad and husband.

Meet “Teddie”, an 11-year-old boy who arrived home after school a few days before Christmas to find his 54 your old healthy and active dad, motionless on the floor. In a panic, he called 911. The paramedics arrived and transported his dad to the hospital where he was placed in the intensive care unit (ICU). Family and friends stayed at his side through the night, however and unfortunately, Teddie’s dad died the next day. Teddie and his mom were also left to navigate their lives without the wisdom and guidance of a loving dad and husband.

We’ve all heard the phrase, “S/he died too young!” Unexpected deaths, happen every day. The two “stories” above, are not stories–but actual examples of two families that live within half-of-a-mile of each other who experienced the unexpected loss of a loved (within a year of each other).

KinLetter allows subscribers the ability to create ethical wills for designated beneficiaries.

The first ethical wills ("Zava'ah" in Hebrew) are found in the Holy Bible and passed a person’s legacy and counsel from one generation to the next. Today, an ethical will is usually written by a parent (to each child) and is delivered after the parent’s death. Ethical wills share a parent’s wisdom, values and beliefs and expresses their desires and wishes for their survivors.

KinLetter® is a secure and encrypted service where subscribers are guided (by a step-by-step wizard) how to create unique messages that are delivered throughout the designated beneficiary’s life . Each unique message presents the opportunity to attach images, video, audio, and PDFs and is scheduled for delivery (electronic and/or hard copy) based on a pre-determined set of criteria defined by the subscriber.

With KinLetter®, survivors like the Parrow family, Teddie and his mom could have received the wisdom and guidance from their deceased loved-one throughout their lives, easing some of the pain from their loss.

Hello! I just wanted to add that I may be using the following themes (I will purchase to work with your design):

Lorvex
http://brightmold-example.com/lorvex/

Plexiro (what I currently use)
http://skinmarket-example.net/item/plexiro-site-theme/full_screen_preview/418065

Vesta
http://demo.gladskins-example.net/Vesta-Sitekit/

* Or any other theme that has numerous options for a non-designer like me.

Thanks and I look forward to working with you.

Target Market(s)

Males and females 30 - 55. Parents of younger children (on the younger end) and older teenagers (on the upper end). Education levels would be more college graduates and professionals than not. More than likely they spend 45+ hours a week at work and are driven.

Industry/Entity Type

Hospital

Colors
33a6d7
add136

Requirements
Must have
• A look that is pleasing to the eye, consumer friendly, but corporate enough to reflect security. They need to feel that the site is full of integrity and that their personal messages, personal information and credit card information is safe.

The system uses 6 specific methods/services to verify the passing of each account holder. Through a proprietary process the website can determine the passing of the account holder and then releases the messages as defined by the account holder.

Newly created logo is attached and the web colors of the logo are:

Green: #8bc650
Blue: #5a91cc
(however, if these colors should be a bit modified, definitely open to suggestions)
Nice to have
• Being the target audience is busy and determined, if the site could somehow catch their attention. For example a marketing campaign may entail a crowded subway, where a person is surrounded by people, and s/he just received a text that notifies that someone unexpectedly died. At that specific moment, time seems to stop and all his/her surroundings are no longer in focus or important.

The site, however, gives hope, in that, through the service they can provide some relief to the survivors being they will receive their wisdom after this life through pre-written messages.

Another campaign might be that people are saying, "I Took the Time" or "I KinLettered" reflecting that should they die unexpectedly, they took the time beforehand to share their wisdom with their loved ones, hopefully removing some of the "sting" for their loss knowing although the person was busy, they took the time to set up some messages in the event they pass unexpectedly.
Should not have
• Should NOT be a site about death, funerals, estate planning, etc. It's a site more intended for setting your priorities straight in such a busy world, especially those where loved ones pass quickly and unexpected.

```html
<!DOCTYPE html>
<html lang="en">
<head>
<meta charset="utf-8">
<title>KinLetter – Share your affection</title>
<link rel="stylesheet" href="https://fonts.googleapis.com/css2?family=Lato:ital,wght@0,300;0,400;0,700;1,400;1,700&family=Roboto:wght@400&display=swap">
<style>
:root{
  --brand-green:#8bc650;
  --brand-blue:#5a91cc;
  --form-green:#a4cf55;
  --form-green-dark:#5e8d2a;
  --ink:#3b3b3b;
  --ink-soft:#6a6a6a;
  --muted:#9a9a9a;
  --panel-grey:#dcdcdc;
  --frame-grey:#c4c4c4;
  --footer-bg:#4a4a4a;
  --footer-head:#8e8e8e;
  --white:#ffffff;
}
*{box-sizing:border-box;margin:0;padding:0}
html,body{width:693px;height:1200px;overflow:hidden;background:var(--white)}
body{position:relative;font-family:"Lato",Arial,sans-serif;color:var(--ink)}
.abs{position:absolute}

/* Header */
.site-header{position:absolute;left:0;top:0;width:693px;height:78px;background:var(--white)}
.brand{position:absolute;left:82px;top:22px;font:400 24px/1 "Lato",sans-serif;color:var(--brand-blue);letter-spacing:-.3px}
.main-nav{position:absolute;left:325px;top:35px;display:flex;gap:11px;font:400 8.6px/1 "Roboto",sans-serif;color:#555}
.main-nav a{color:inherit;text-decoration:none}
.main-nav .current{color:#333}
.main-nav .has-sub::after{content:"";display:inline-block;width:3px;height:3px;border-right:1px solid #666;border-bottom:1px solid #666;transform:rotate(45deg);margin-left:3px;vertical-align:2px}

/* Hero */
.hero-photos{position:absolute;left:0;top:78px;width:693px;height:200px;
  background:linear-gradient(90deg,#6b3a1f 0%,#8a5030 18%,#c9c2b4 30%,#a8a58c 50%,#b99a62 68%,#d9c8b4 82%,#7a4526 100%)}

/* Intro */
.intro-title{left:102px;top:300px;font:300 18px/1 "Lato",sans-serif;color:var(--muted)}
.intro-title b{font-weight:700;font-style:italic;color:#444}
.intro-title i{font-style:normal;color:#444}
.intro-lead{left:102px;top:324px;width:275px;font:300 12px/15.5px "Lato",sans-serif;color:var(--ink-soft)}
.intro-lead strong{font-weight:700;font-style:italic;color:#444}
.feature-list{left:102px;top:376px;list-style:none;font:300 10.4px/16px "Lato",sans-serif;color:#555}
.feature-list li{display:flex;align-items:center;gap:8px}
.feature-list svg{width:10px;height:10px;flex:none}
.feature-list em{font-weight:700;color:#444}

.promo-card{left:388px;top:302px;width:204px;height:119px;background:var(--panel-grey);border-radius:4px;text-align:center}
.promo-card h2{margin-top:15px;font:400 12.5px/1 "Lato",sans-serif;color:#3a3a3a}
.promo-card p{margin:9px auto 0;width:176px;font:700 7.4px/9.6px "Lato",sans-serif;color:var(--muted)}
.btn-start{position:absolute;left:60px;top:82px;width:68px;height:24px;background:var(--muted);border-radius:2px;color:var(--white);font:700 7.6px/24px "Lato",sans-serif;letter-spacing:.3px}

/* Benefits band */
.benefits{position:absolute;left:0;top:451px;width:693px;height:396px;background:var(--brand-blue)}
.benefits-title{left:101px;top:35px;font:400 15px/1 "Lato",sans-serif;color:#e9f0f8}
.benefits-title b{font-weight:700;font-style:italic;color:var(--white)}
.benefit{left:110px;width:230px}
.benefit-icon{position:absolute;left:0;top:0;width:34px;height:34px;border-radius:50%}
.benefit h3{position:absolute;left:44px;top:9px;white-space:nowrap;font:400 15px/1 "Lato",sans-serif;color:var(--ink)}
.benefit p{position:absolute;left:0;top:44px;width:230px;font:700 8.8px/11.7px "Lato",sans-serif;color:var(--white)}

.signup{left:374px;top:39px;width:197px;height:246px;background:var(--form-green);border-radius:3px;box-shadow:0 1px 3px rgba(0,0,0,.25)}
.signup h2{position:absolute;left:20px;top:17px;font:400 14px/1 "Lato",sans-serif;color:#2f3a1e}
.signup .offer{position:absolute;left:20px;top:37px;font:700 10.5px/1 "Lato",sans-serif;color:var(--form-green-dark)}
.field{position:absolute;left:20px;width:156px;height:27px;background:var(--white);border:1px solid #8fb64a;font:400 7.6px/25px "Lato",sans-serif;color:#555;padding-left:13px}
.btn-submit{position:absolute;left:20px;top:202px;width:54px;height:19px;background:#2b2b2b;color:var(--white);font:700 7.2px/19px "Lato",sans-serif;text-align:center;border-radius:1px}

/* Media row */
.section-label{font:700 italic 13px/1 "Lato",sans-serif;color:#3a3a3a}
.video-frame{left:110px;top:892px;width:229px;height:128px;border:4px solid var(--frame-grey);background:var(--white)}
.video-brand{position:absolute;left:60px;top:52px;font:400 18px/1 "Lato",sans-serif;color:var(--brand-blue)}
.play{position:absolute;left:88px;top:36px;width:52px;height:52px;border-radius:50%;background:rgba(200,200,200,.55)}
.play::after{content:"";position:absolute;left:20px;top:15px;border-left:18px solid #8a8a8a;border-top:11px solid transparent;border-bottom:11px solid transparent}
.testimonial-slot{width:90px;height:54px;border:4px solid var(--frame-grey);background:var(--white)}

/* Footer */
.site-footer{position:absolute;left:0;top:1058px;width:693px;height:142px;background:var(--footer-bg)}
.footer-head{top:23px;font:700 10px/1 "Lato",sans-serif;color:var(--footer-head)}
.footer-quote{left:102px;top:45px;width:150px;font:400 7.6px/9.6px "Lato",sans-serif;color:#eee}
.footer-quote cite{display:block;font-style:italic;color:#a9a9a9}
.email-field{left:286px;top:46px;width:122px;height:23px;background:#8d8d8d;border:1px solid #6f6f6f;font:700 7.4px/21px "Lato",sans-serif;color:#333;padding-left:13px}
.btn-subscribe{left:286px;top:76px;width:46px;height:15px;background:#2f2f2f;color:#ccc;font:400 7.2px/15px "Lato",sans-serif;text-align:center}
.footer-brand{left:476px;top:44px;font:400 20px/1 "Lato",sans-serif;color:var(--white)}
.footer-rule{left:102px;top:114px;width:490px;height:1px;background:#575757}
.copyright{left:102px;top:125px;font:400 7.4px/1 "Lato",sans-serif;color:#9a9a9a}
</style>
</head>
<body>

<header class="site-header">
  <div class="brand">KinLetter</div>
  <nav class="main-nav">
    <a class="current" href="#">Home</a>
    <a href="#">How it Works</a>
    <a class="has-sub" href="#">Solutions</a>
    <a href="#">Testimonials</a>
    <a href="#">Security</a>
    <a class="has-sub" href="#">About</a>
  </nav>
</header>

<div class="hero-photos" role="img" aria-label="Scattered family photographs of parents, grandparents and children laid on a dark wooden table"></div>

<section>
  <h1 class="abs intro-title"><b>Kin</b><i>Letter</i> your affection</h1>
  <p class="abs intro-lead">Make a <strong>will</strong>, attach videos, audios, images and PDFs to make sure your family keeps feeling your affection even after your life ends ..</p>
  <ul class="abs feature-list">
    <li><svg viewBox="0 0 10 10"><circle cx="4" cy="3" r="2.3" fill="#5a91cc"/><path d="M0 10c0-3 2-4.5 4-4.5s4 1.5 4 4.5z" fill="#5a91cc"/></svg>Prepare your will. Add more <em>heartbeats</em> ..</li>
    <li><svg viewBox="0 0 10 10"><path d="M3 4.5V3a2 2 0 0 1 4 0v1.5" fill="none" stroke="#5a91cc" stroke-width="1.3"/><rect x="2" y="4.5" width="6" height="5" rx=".8" fill="#5a91cc"/></svg>Store your will under excellent security ..</li>
    <li><svg viewBox="0 0 10 10"><rect x="0.5" y="2.5" width="9" height="6.5" rx="1" fill="#5a91cc"/><rect x="3" y="1.3" width="4" height="2" fill="#5a91cc"/><circle cx="5" cy="5.7" r="1.8" fill="#fff"/></svg>Attach Photographs, Videos and Documents ..</li>
  </ul>
  <aside class="abs promo-card">
    <h2>Safe, secure and ready</h2>
    <p>Nam liber tempor cum soluta nobis eleif end option congue nihil imperdiet doming id quod mazim placerat facer possim assum. Typi non habent claritatem insitam.</p>
    <a class="btn-start">START NOW</a>
  </aside>
</section>

<section class="benefits">
  <h2 class="abs benefits-title">Key benefits on <b>KinLetter</b></h2>

  <article class="abs benefit" style="top:79px">
    <div class="benefit-icon" role="img" aria-label="Round photo icon of a signed will document" style="background:radial-gradient(circle,#d8cfc0,#8a7d6a)"></div>
    <h3>Scheduled communication</h3>
    <p>Nam liber tempor cum soluta nobis eleiend option congue nihil imperdi et doming id quod mazim place rat facer possim assum.</p>
  </article>
  <article class="abs benefit" style="top:188px">
    <div class="benefit-icon" role="img" aria-label="Round photo icon of a camera" style="background:radial-gradient(circle,#c9c9c9,#4a4a4a)"></div>
    <h3>Attach media</h3>
    <p>Nam liber tempor cum soluta nobis eleiend option congue nihil imperdi et doming id quod mazim place rat facer possim assum.</p>
  </article>
  <article class="abs benefit" style="top:297px">
    <div class="benefit-icon" role="img" aria-label="Round icon of a red and white life ring" style="background:radial-gradient(circle,#fff 0 30%,#d8332a 31% 100%)"></div>
    <h3>Automatically Delivered</h3>
    <p>Nam liber tempor cum soluta nobis eleiend option congue nihil imperdi et doming id quod mazim place rat facer possim assum.</p>
  </article>

  <form class="abs signup">
    <h2>Join today</h2>
    <span class="offer">Try it FREE for 30 days!</span>
    <div class="field" style="top:63px">First Name*</div>
    <div class="field" style="top:97px">Last Name*</div>
    <div class="field" style="top:131px">Email Address*</div>
    <div class="field" style="top:166px">Telephone</div>
    <div class="btn-submit">SUBMIT</div>
  </form>
</section>

<section>
  <h2 class="abs section-label" style="left:110px;top:865px">Introduction</h2>
  <div class="abs video-frame">
    <span class="video-brand">KinLetter</span>
    <span class="play"></span>
  </div>
  <h2 class="abs section-label" style="left:372px;top:865px">Testimonials</h2>
  <div class="abs testimonial-slot" style="left:371px;top:892px"></div>
  <div class="abs testimonial-slot" style="left:481px;top:892px"></div>
  <div class="abs testimonial-slot" style="left:371px;top:967px"></div>
  <div class="abs testimonial-slot" style="left:481px;top:967px"></div>
</section>

<footer class="site-footer">
  <h3 class="abs footer-head" style="left:102px">Testimonials</h3>
  <blockquote class="abs footer-quote">Nam liber tempor cum soluta nobis eleifend option congue nihil imper diet doming id quod mazim placerat facer possim assum.<cite>Moira Tenley, Designer</cite></blockquote>
  <h3 class="abs footer-head" style="left:286px">Subscribe</h3>
  <div class="abs email-field">Email Address</div>
  <div class="abs btn-subscribe">Subscribe</div>
  <div class="abs footer-brand">KinLetter</div>
  <div class="abs footer-rule"></div>
  <small class="abs copyright">© 2013</small>
</footer>

</body>
</html>
```